Consulting company requires a logo and business card design

I require a logo/business card design for a new company based in Sexsmith Alberta called TanRidge Field Advisory Ltd. I plan to provide the following services: Construction management/inspection for the oil and gas industry, as well as general consulting for Asset Management, fleet management, etc. Have attached a copy of resume for use as guide for

Target Market(s)

Businesses within the oil and gas production, construction and shipping industry

Industry/Entity Type

Oil And Gas

Contact Information for Business Card

Believe should highlight, services offered, safety, quality,

Logo Text

TanRidge Field Advisory (TRFA) ?

Font styles to use
Script

Requirements
Must have
• Open to all options

```html
<!DOCTYPE html>
<html lang="en">
<head>
<meta charset="utf-8">
<title>TanRidge Field Advisory Ltd. – Business Card</title>
<link href="https://fonts.googleapis.com/css2?family=Source+Sans+3:wght@400;600&display=swap" rel="stylesheet">
<style>
  :root {
    --backdrop: #e4e4e4;
    --card: #000000;
    --sky: #5cb8ec;
    --sky-soft: #6fa9e2;
    --ember: #e8542a;
    --ink: #ffffff;
  }
  * { margin: 0; padding: 0; box-sizing: border-box; }
  html, body { width: 1200px; height: 900px; overflow: hidden; }
  body {
    background: var(--backdrop);
    font-family: "Source Sans 3", Arial, sans-serif;
    color: var(--ink);
    position: relative;
  }
  .card {
    position: absolute;
    top: 306px;
    width: 440px;
    height: 271px;
    background: var(--card);
    border-radius: 12px;
  }
  .card--front { left: 149px; }
  .card--back { left: 608px; }

  .brand { position: absolute; text-align: center; color: var(--sky); font-weight: 400; }
  .brand__dot { display: block; margin: 0 auto; border-radius: 50%; background: var(--sky); }
  .brand__name { display: block; line-height: 1; }
  .brand__sub { display: block; letter-spacing: 2.2px; line-height: 1; }

  .card--front .brand { left: 20px; width: 205px; top: 86px; }
  .card--front .brand__dot { width: 26px; height: 26px; margin-bottom: 30px; }
  .card--front .brand__name { font-size: 30px; }
  .card--front .brand__sub { font-size: 11.5px; margin-top: 10px; letter-spacing: 1.6px; }

  .details { position: absolute; left: 233px; top: 40px; font-size: 13px; line-height: 16px; }
  .details__name { color: var(--sky); font-size: 18px; font-weight: 600; line-height: 22px; }
  .details__role { margin-top: 2px; }
  .details__address { margin-top: 17px; }
  .contacts { list-style: none; margin-top: 11px; }
  .contacts li { display: flex; align-items: center; gap: 10px; }
  .contacts svg { width: 10px; height: 10px; fill: var(--sky); flex: none; }

  .card--back .brand { left: 0; width: 100%; top: 34px; }
  .card--back .brand__dot { width: 34px; height: 34px; margin-bottom: 40px; }
  .card--back .brand__name { font-size: 34px; }
  .card--back .brand__sub { font-size: 13px; margin-top: 10px; }
  .services {
    position: absolute; left: 30px; right: 30px; top: 188px;
    text-align: center; color: var(--sky-soft); font-size: 12.5px; line-height: 16px;
  }
</style>
</head>
<body>
  <section class="card card--front">
    <div class="brand">
      <span class="brand__dot"></span>
      <span class="brand__name">TanRidge</span>
      <span class="brand__sub">Field Advisory Ltd.</span>
    </div>
    <div class="details">
      <p class="details__name">Marcus Delaney</p>
      <p class="details__role">Managing Director</p>
      <p class="details__address">1234, Address Goes Here<br>Country Name, 123456</p>
      <ul class="contacts">
        <li><svg viewBox="0 0 10 10"><rect x="2.5" y="0.5" width="5" height="9" rx="1"/></svg>123-456-7890</li>
        <li><svg viewBox="0 0 10 10"><path d="M1 4c0-2 2-3 4-3s4 1 4 3H7V3H3v1zM2 5h6l1 4H1z"/></svg>123-456-7890</li>
        <li><svg viewBox="0 0 10 10"><path d="M3 0h4v3H3zM1 3h8v6H1z"/></svg>123-456-7890</li>
        <li><svg viewBox="0 0 10 10"><path d="M0 2h10v6H0zM0 2l5 3 5-3"/></svg>info@youremail.com</li>
        <li><svg viewBox="0 0 10 10"><path d="M1 9l3-3-1-1 3-3 2 2-3 3-1-1-3 3z"/></svg>www.yourweb.com</li>
      </ul>
    </div>
  </section>

  <section class="card card--back">
    <div class="brand">
      <span class="brand__dot"></span>
      <span class="brand__name">TanRidge</span>
      <span class="brand__sub">Field Advisory Ltd.</span>
    </div>
    <p class="services">We are a construction management/inspection for the oil and gas industry, as well as general consulting for Asset Management, fleet management.</p>
  </section>
</body>
</html>
```